business card for an electronic retail store

take our existing color logo, design a new business card and make a black&white version of the logo as well

Industry/Entity Type

Electronic

```html
<!DOCTYPE html>
<html lang="en">
<head>
<meta charset="utf-8">
<title>Velocitron Business Card</title>
<link rel="stylesheet" href="https://fonts.googleapis.com/css2?family=Arimo:wght@400;700&family=Crimson+Text:wght@600&family=Roboto+Condensed:wght@700&display=swap">
<style>
  :root {
    --backdrop: #2f3d47;
    --card-black: #242424;
    --card-yellow: #f8da0c;
    --ink: #1f1f1f;
    --paper: #ffffff;
    --accent-red: #d9232a;
    --sans: "Arimo", Arial, sans-serif;
    --serif: "Crimson Text", Georgia, serif;
    --condensed: "Roboto Condensed", "Arial Narrow", sans-serif;
  }
  * { box-sizing: border-box; margin: 0; padding: 0; }
  html, body {
    width: 1200px; height: 1000px; overflow: hidden;
    background: var(--backdrop);
  }
  .sheet {
    width: 1200px; height: 1000px;
    display: flex; flex-direction: column; align-items: center;
    justify-content: center; gap: 28px;
  }
  .card {
    position: relative;
    width: 800px; height: 457px;
    border-radius: 4px;
    box-shadow: 0 10px 30px rgba(0,0,0,0.35);
  }
  .card--front { background: var(--card-black); color: var(--paper); }
  .card--back { background: var(--card-yellow); color: var(--ink); }

  .brand {
    position: absolute; left: 0; right: 0;
    display: flex; flex-direction: column; align-items: center;
  }
  .card--front .brand { top: 120px; }
  .card--back .brand { top: 34px; }
  .brand__mark { display: flex; align-items: center; gap: 16px; }
  .brand__square { width: 44px; height: 44px; background: var(--accent-red); }
  .brand__name {
    font-family: var(--sans); font-weight: 700;
    font-size: 76px; letter-spacing: 2px; line-height: 1;
  }
  .card--front .brand__name { color: var(--card-yellow); }
  .card--back .brand__name { color: var(--ink); }
  .brand__tagline {
    margin-top: 14px;
    font-family: var(--serif); font-weight: 600;
    font-size: 28px; letter-spacing: 1.5px;
  }

  .contact { position: absolute; left: 40px; bottom: 30px; }
  .contact__call { display: flex; align-items: flex-start; gap: 12px; }
  .contact__call-label {
    font-family: var(--sans); font-weight: 700; font-size: 30px; line-height: 1;
  }
  .contact__phone {
    font-family: var(--condensed); font-weight: 700; font-size: 40px; line-height: 1.05;
  }
  .contact__row { display: flex; align-items: center; gap: 22px; margin-top: 14px; }
  .contact__address, .contact__email {
    font-family: var(--sans); font-size: 22px; line-height: 1.35;
  }
  .icon { fill: none; stroke: var(--ink); stroke-width: 3; flex-shrink: 0; }
  .icon--solid { fill: var(--ink); stroke: none; }

  .person {
    position: absolute; right: 48px; bottom: 92px; text-align: right;
    font-family: var(--sans);
  }
  .person__name { font-weight: 700; font-size: 29px; }
  .person__role { font-size: 21px; margin-top: 6px; }
  .person__line {
    display: flex; justify-content: flex-end; align-items: center; gap: 12px;
    font-size: 23px; margin-top: 8px;
  }
</style>
</head>
<body>
<main class="sheet">
  <section class="card card--front">
    <div class="brand">
      <div class="brand__mark">
        <span class="brand__square"></span>
        <span class="brand__name">VELOCITRON</span>
      </div>
      <p class="brand__tagline">Car Audio • Performance • Security</p>
    </div>
  </section>

  <section class="card card--back">
    <div class="brand">
      <div class="brand__mark">
        <span class="brand__square"></span>
        <span class="brand__name">VELOCITRON</span>
      </div>
      <p class="brand__tagline">Car Audio • Performance • Security</p>
    </div>

    <div class="contact">
      <div class="contact__call">
        <svg class="icon" width="40" height="40" viewBox="0 0 40 40" aria-hidden="true">
          <circle cx="20" cy="20" r="17"/>
          <path class="icon--solid" d="M14 11c1-1 2-1 3 0l2 3c.5 1 0 2-1 2.5l-1 .5c1 3 3 5 5 6l.6-1c.5-1 1.5-1.3 2.4-.8l3 2c1 .6 1 1.8 0 2.8-2 2-4 2-7 0-4-2.5-7-6-8-10-.5-2 0-4 1-5z"/>
        </svg>
        <div>
          <p class="contact__call-label">CALL US</p>
          <p class="contact__phone">555-014-2730</p>
        </div>
      </div>
      <div class="contact__row">
        <svg width="26" height="40" viewBox="0 0 26 40" aria-hidden="true">
          <path class="icon--solid" d="M13 0C6 0 0 5.5 0 12.5 0 21 13 40 13 40s13-19 13-27.5C26 5.5 20 0 13 0zm0 18a5.5 5.5 0 1 1 0-11 5.5 5.5 0 0 1 0 11z"/>
        </svg>
        <p class="contact__address">Harbor Point Plaza<br>1420 Ridge Road<br>Bayview Twp 08000</p>
      </div>
      <div class="contact__row">
        <svg width="36" height="26" viewBox="0 0 36 26" aria-hidden="true">
          <rect class="icon--solid" x="0" y="0" width="36" height="26" rx="2"/>
          <path d="M2 2l16 13L34 2" fill="none" stroke="#f8da0c" stroke-width="2.5"/>
        </svg>
        <p class="contact__email">hello@velocitron.example</p>
      </div>
    </div>

    <div class="person">
      <p class="person__name">Daniel Marsh</p>
      <p class="person__role">Position</p>
      <p class="person__line">daniel@velocitron.example
        <svg width="22" height="16" viewBox="0 0 22 16" aria-hidden="true">
          <rect class="icon--solid" width="22" height="16" rx="1"/>
          <path d="M1 1l10 8 10-8" fill="none" stroke="#f8da0c" stroke-width="2"/>
        </svg>
      </p>
      <p class="person__line">123 456 7800
        <svg width="16" height="26" viewBox="0 0 16 26" aria-hidden="true">
          <rect x="1.5" y="1.5" width="13" height="23" rx="2.5" fill="none" stroke="#1f1f1f" stroke-width="2"/>
          <line x1="6" y1="21" x2="10" y2="21" stroke="#1f1f1f" stroke-width="2"/>
        </svg>
      </p>
    </div>
  </section>
</main>
</body>
</html>
```